Double-sided business card needed - specific brief

We need a double sided business card designed for our company Radiant Trimline. Having lost a lot of weight myself, the back of the card needs to show my before and after pictures. It needs to cover the entire back side of the card. This might be with my two before pictures over set on top of my main after picture or in separate frames. I'll leave that to your artistic consideration. The front needs to have our logo with contact details centred below.

The cards will be printed by PRINTKO.com and will be rectangular, 84mm x 55mm, but with ROUNDED edges. Please therefore present your designs rectangular but with rounded edges if possible.

The card should be designed in LANDSCAPE orientation.

As well as the logo, the front of the card should have the following details:

Moira Blakewell
Weight Loss Motivator with 189lb personal loss
moira@radiant-trimline.example
+44 (0)7700 900418

The website is important so should perhaps be more bold than the rest:
www.radiant-trimline.example

My brand colours are: Pink #CD2366, Light Pink #FD88AD. Blue #1C9CB1, Light Blue #64C4DE

Target Market(s)

Women 30+

Contact Information for Business Card

As description above

Font styles to use
Sans Serif

Requirements
Must have
• Double sided.
• Back side entirely covered with my before and after pictures.
• You may wish to float my before pictures on top of my after picture or add them in different frames. I look forward to seeing your different suggestions.

```html
<!DOCTYPE html>
<html lang="en">
<head>
<meta charset="utf-8">
<title>Radiant Trimline – Business Card</title>
<link href="https://fonts.googleapis.com/css2?family=PT+Sans:wght@400;700&family=Tinos:wght@400&display=swap" rel="stylesheet">
<style>
  :root {
    --pink: #CD2366;
    --pink-deep: #C41F5F;
    --light-pink: #FD88AD;
    --blue: #1C9CB1;
    --light-blue: #64C4DE;
    --white: #FFFFFF;
    --stage: #E6E6E6;
    --ink-soft: #F4D3E0;
  }
  * { margin: 0; padding: 0; box-sizing: border-box; }
  html, body { width: 1200px; height: 900px; overflow: hidden; }
  body {
    background: var(--stage);
    font-family: "PT Sans", sans-serif;
    position: relative;
  }
  .card {
    position: absolute;
    top: 273px;
    width: 540px;
    height: 354px;
    border-radius: 26px;
    overflow: hidden;
    background: var(--white);
    box-shadow: 0 2px 6px rgba(0,0,0,0.12);
  }
  .card--front { left: 40px; }
  .card--back { left: 620px; }

  /* Front */
  .front__brand-panel {
    position: absolute; left: 0; top: 0; width: 215px; height: 100%;
    background: var(--white);
  }
  .front__info-panel {
    position: absolute; left: 215px; top: 0; right: 0; height: 100%;
    background: var(--pink);
  }
  .brand {
    position: absolute; left: 28px; top: 96px; width: 170px;
    display: flex; flex-direction: column; align-items: center; gap: 10px;
  }
  .brand__dot {
    width: 42px; height: 42px; border-radius: 50%;
    background: var(--pink);
  }
  .brand__name {
    font-family: "Tinos", serif;
    font-size: 21px; line-height: 1.1;
    color: var(--pink);
    text-transform: uppercase; text-align: center; letter-spacing: 0.5px;
  }
  .social {
    display: flex; gap: 8px; margin-top: 4px;
  }
  .social__tile {
    width: 15px; height: 15px; border-radius: 3px; background: var(--pink);
  }
  .person {
    position: absolute; left: 255px; top: 40px;
  }
  .person__name {
    font-family: "Tinos", serif;
    font-size: 25px; color: var(--white);
    text-transform: uppercase; letter-spacing: 1px;
  }
  .person__role {
    margin-top: 6px;
    font-size: 14px; line-height: 1.3; color: var(--light-blue);
  }
  .contacts {
    position: absolute; left: 195px; top: 150px;
    list-style: none;
  }
  .contact {
    display: flex; align-items: center; height: 40px; margin-bottom: 10px;
  }
  .contact__tab {
    width: 42px; height: 34px; background: var(--blue);
    display: flex; align-items: center; justify-content: center;
    box-shadow: 2px 2px 3px rgba(0,0,0,0.18);
  }
  .contact__tab svg { width: 20px; height: 20px; }
  .contact__text {
    margin-left: 18px; font-size: 16px; color: var(--white);
  }
  .contact__text--web { font-weight: 700; }

  /* Back */
  .photo {
    position: absolute;
    border: 3px solid;
  }
  .photo--before {
    left: 20px; top: 20px; width: 285px; height: 225px;
    border-color: var(--pink);
    background: linear-gradient(160deg, #6E7A4E 0%, #B9B2A2 40%, #F1EFEA 60%, #5F7B3C 100%);
  }
  .photo--after {
    left: 250px; top: 58px; width: 270px; height: 258px;
    border-color: var(--blue);
    background: linear-gradient(150deg, #C9B79A 0%, #8B6645 45%, #2B3A66 75%, #1F2A4F 100%);
  }
  .label {
    position: absolute; font-size: 15px;
  }
  .label--before { left: 120px; top: 256px; color: var(--pink); }
  .label--after { left: 370px; top: 324px; color: var(--blue); }
  .back__brand {
    position: absolute; left: 60px; top: 298px;
    display: flex; align-items: center; gap: 6px;
  }
  .back__brand-dot { width: 12px; height: 12px; border-radius: 50%; background: var(--pink); }
  .back__brand-name {
    font-family: "Tinos", serif; font-size: 14px; color: var(--pink);
    text-transform: uppercase; letter-spacing: 0.5px;
  }
</style>
</head>
<body>

<section class="card card--front" aria-label="Card front">
  <div class="front__brand-panel">
    <div class="brand">
      <span class="brand__dot"></span>
      <span class="brand__name">Radiant<br>Trimline</span>
      <div class="social">
        <span class="social__tile"></span>
        <span class="social__tile"></span>
        <span class="social__tile"></span>
      </div>
    </div>
  </div>
  <div class="front__info-panel"></div>

  <div class="person">
    <p class="person__name">Moira Blakewell</p>
    <p class="person__role">Weight Loss Motivator<br>(with 189lb personal loss)</p>
  </div>

  <ul class="contacts">
    <li class="contact">
      <span class="contact__tab">
        <svg viewBox="0 0 20 20" fill="none" stroke="#fff" stroke-width="1.6"><rect x="2" y="4.5" width="16" height="11" rx="1"/><path d="M2 5l8 6 8-6"/></svg>
      </span>
      <span class="contact__text">moira@radiant-trimline.example</span>
    </li>
    <li class="contact">
      <span class="contact__tab">
        <svg viewBox="0 0 20 20" fill="#fff"><path d="M5 3h3l1.5 4-2 1.3a9 9 0 0 0 4.2 4.2l1.3-2 4 1.5v3a2 2 0 0 1-2 2A14 14 0 0 1 3 5a2 2 0 0 1 2-2z"/></svg>
      </span>
      <span class="contact__text">+44 (0)7700 900418</span>
    </li>
    <li class="contact">
      <span class="contact__tab">
        <svg viewBox="0 0 20 20" fill="none" stroke="#fff" stroke-width="1.4"><circle cx="10" cy="10" r="7.5"/><ellipse cx="10" cy="10" rx="3.2" ry="7.5"/><path d="M2.5 10h15M4 6h12M4 14h12"/></svg>
      </span>
      <span class="contact__text contact__text--web">www.radiant-trimline.example</span>
    </li>
  </ul>
</section>

<section class="card card--back" aria-label="Card back">
  <div class="photo photo--before" role="img" aria-label="Before photo of Moira Blakewell in a garden"></div>
  <div class="photo photo--after" role="img" aria-label="After photo of Moira Blakewell seated on a leather sofa"></div>
  <span class="label label--before">Before</span>
  <span class="label label--after">After</span>
  <div class="back__brand">
    <span class="back__brand-dot"></span>
    <span class="back__brand-name">Radiant Trimline</span>
  </div>
</section>

</body>
</html>
```